Children's martial arts flyer for new classes

Need a postcard flyer addressing the attached spec (see file).

Flyer needs to be Postcard Size and be suited in style to the target demographic which is parents of children aged 5-12 years old.

Classes are new.

Postcard must include the logo and a picture. I have included an example pic in the attached file, but feel free to use other suitable pics.

Target Market(s)

Parents with children aged 5-12 years old

Colors

Designer to choose colors to be used in the design.

Requirements
Must have
• clean look.
• professional.

```html
<!DOCTYPE html>
<html lang="en">
<head>
<meta charset="utf-8">
<title>Kicks Dojo – Children's Martial Art Classes Postcard</title>
<link href="https://fonts.googleapis.com/css2?family=Open+Sans:wght@300;400;600;700;800&family=Fredoka:wght@600&display=swap" rel="stylesheet">
<style>
  :root{
    --page:#ffffff;
    --card-edge:#e4e4e4;
    --amber:#efb23a;
    --slate:#6e6e6e;
    --map-dark:#242424;
    --ink:#2a1f14;
    --ink-soft:#3a2c16;
    --white:#ffffff;
  }
  *{margin:0;padding:0;box-sizing:border-box}
  html,body{width:1200px;height:1200px;overflow:hidden;background:var(--page)}
  body{position:relative;font-family:"Open Sans",Arial,sans-serif;color:var(--ink)}
  .size-label{position:absolute;top:34px;left:0;width:1200px;text-align:center;
    font-family:Arial,Helvetica,sans-serif;font-size:45px;color:#111;letter-spacing:.5px}
  .postcard{position:absolute;left:240px;width:720px;height:480px;background:var(--white);
    box-shadow:0 0 0 1px var(--card-edge),0 1px 3px rgba(0,0,0,.06)}
  .postcard--front{top:114px}
  .postcard--back{top:650px}
  .postcard svg.art{position:absolute;left:0;top:0}
  .abs{position:absolute}
  .brand{left:48px;display:flex;align-items:center;gap:9px;
    font-weight:800;font-size:16px;color:var(--white)}
  .postcard--front .brand{top:62px}
  .postcard--back .brand{top:80px}
  .brand-dot{width:30px;height:30px;border-radius:50%;background:var(--amber)}
  .photo-title{left:34px;top:372px;font-family:"Fredoka",sans-serif;font-weight:600;font-size:31px;
    line-height:42px;color:var(--white)}
  .headline{right:50px;top:46px;text-align:right;font-weight:800;font-size:36px;
    line-height:42px;color:var(--ink)}
  .subhead{right:50px;top:136px;font-weight:400;font-size:16px;color:var(--ink-soft)}
  .schedule{right:146px;top:175px;text-align:right;font-weight:700;font-size:11px;line-height:14px}
  .phone{right:150px;top:250px;text-align:right}
  .phone-number{font-weight:700;font-size:20px;line-height:23px}
  .phone-note{font-weight:400;font-size:10.5px;line-height:13px;letter-spacing:.2px}
  .contact-line{right:70px;font-size:11.5px;font-weight:400;color:var(--ink);white-space:nowrap}
  .contact-line--address{top:403px}
  .contact-line--web{top:433px}
</style>
</head>
<body>

<div class="size-label">6 inch X 4 inch</div>

<!-- Front of postcard -->
<section class="postcard postcard--front">
  <svg class="art" width="720" height="480" viewBox="0 0 720 480">
    <defs>
      <linearGradient id="kidsBackdrop" x1="0" y1="0" x2="1" y2=".4">
        <stop offset="0" stop-color="#1f7fa6"/>
        <stop offset=".6" stop-color="#3db3d6"/>
        <stop offset="1" stop-color="#7fd6ee"/>
      </linearGradient>
      <radialGradient id="kidsUniforms" cx=".45" cy=".78" r=".62">
        <stop offset="0" stop-color="#f1efec"/>
        <stop offset=".45" stop-color="#dcd3cb" stop-opacity=".9"/>
        <stop offset=".75" stop-color="#c9a98f" stop-opacity=".45"/>
        <stop offset="1" stop-color="#c9a98f" stop-opacity="0"/>
      </radialGradient>
      <linearGradient id="kidsBelts" x1="0" y1="0" x2="0" y2="1">
        <stop offset="0" stop-color="#e4572e" stop-opacity="0"/>
        <stop offset=".5" stop-color="#e4572e" stop-opacity=".35"/>
        <stop offset="1" stop-color="#e4572e" stop-opacity="0"/>
      </linearGradient>
      <linearGradient id="titleShade" x1="0" y1="0" x2="0" y2="1">
        <stop offset="0" stop-color="#000" stop-opacity="0"/>
        <stop offset="1" stop-color="#000" stop-opacity=".7"/>
      </linearGradient>
      <linearGradient id="mapTone" x1="0" y1="0" x2="1" y2="1">
        <stop offset="0" stop-color="#2b2b2b"/>
        <stop offset=".5" stop-color="#222"/>
        <stop offset="1" stop-color="#2e2e2e"/>
      </linearGradient>
      <clipPath id="frontPhotoClip"><polygon points="24,22 357,22 299,456 24,456"/></clipPath>
    </defs>
    <rect x="24" y="22" width="672" height="434" fill="var(--amber)"/>
    <rect x="330" y="306" width="366" height="90" fill="url(#mapTone)" role="img" aria-label="Street map of the class location"/>
    <g clip-path="url(#frontPhotoClip)" role="img" aria-label="Photo of three children in white uniforms with coloured belts throwing punches">
      <rect x="24" y="22" width="340" height="434" fill="url(#kidsBackdrop)"/>
      <rect x="24" y="22" width="340" height="434" fill="url(#kidsUniforms)"/>
      <rect x="24" y="330" width="340" height="80" fill="url(#kidsBelts)"/>
      <rect x="24" y="340" width="340" height="116" fill="url(#titleShade)"/>
    </g>
    <polygon points="360,0 438,0 306,456 296,480" fill="var(--slate)"/>
    <line x1="594" y1="174" x2="594" y2="223" stroke="var(--ink)" stroke-width="1.5"/>
    <rect x="610" y="166" width="57" height="57" fill="none" stroke="var(--ink)" stroke-width="1.6"/>
    <circle cx="638.5" cy="194.5" r="9" fill="none" stroke="var(--ink)" stroke-width="2.2"/>
    <path d="M638.5 189v6h-4" fill="none" stroke="var(--ink)" stroke-width="2"/>
    <line x1="594" y1="248" x2="594" y2="296" stroke="var(--ink)" stroke-width="1.5"/>
    <rect x="610" y="238" width="57" height="57" fill="none" stroke="var(--ink)" stroke-width="1.6"/>
    <path d="M632 259c1-1 2-1 3 0l2 3c.5 1 0 2-1 2.5-1 .5 0 3 2 5s4.5 2.5 5 1.5c.5-1 1.5-1.5 2.5-1l3 2c1 1 1 2 0 3-2 2-5 2-9-1.5s-6.5-8-7.5-10.5c-.5-2 0-3 0-4z" fill="var(--ink)"/>
    <rect x="654" y="403" width="14" height="14" fill="none" stroke="var(--ink)" stroke-width="1"/>
    <path d="M661 405.5c-2 0-3.3 1.5-3.3 3.2 0 2.3 3.3 5.3 3.3 5.3s3.3-3 3.3-5.3c0-1.7-1.3-3.2-3.3-3.2z" fill="none" stroke="var(--ink)" stroke-width="1.1"/>
    <rect x="654" y="433" width="14" height="14" fill="none" stroke="var(--ink)" stroke-width="1"/>
  </svg>

  <div class="abs brand"><span class="brand-dot"></span>Kicks Dojo</div>
  <div class="abs photo-title">Children’s martial<br>art classes</div>

  <h1 class="abs headline">FUN AND<br>EXCITING YET</h1>
  <p class="abs subhead">CONTROLLED AND DISCIPLINED</p>
  <p class="abs schedule">TUESDAY’S AND<br>THURSDAY’S<br>6.00 PM</p>
  <div class="abs phone">
    <p class="phone-number">0400 218 545</p>
    <p class="phone-note">TO BOOK A FREE TRIAL CLASS</p>
  </div>
  <p class="abs contact-line contact-line--address">4/18, Harbour View Road Kensington VIC 3099 |</p>
  <p class="abs contact-line contact-line--web">https://www.kicksdojo.example/KIDS |</p>
</section>

<!-- Back of postcard -->
<section class="postcard postcard--back">
  <svg class="art" width="720" height="480" viewBox="0 0 720 480">
    <defs>
      <linearGradient id="wallTone" x1="0" y1="0" x2="1" y2="1">
        <stop offset="0" stop-color="#9c9c9c"/>
        <stop offset=".5" stop-color="#bdbcba"/>
        <stop offset="1" stop-color="#8a8988"/>
      </linearGradient>
      <radialGradient id="fighterGlow" cx=".72" cy=".5" r=".5">
        <stop offset="0" stop-color="#f4f3f1"/>
        <stop offset=".5" stop-color="#e6e4e1" stop-opacity=".8"/>
        <stop offset="1" stop-color="#e6e4e1" stop-opacity="0"/>
      </radialGradient>
      <radialGradient id="gloveTone" cx=".82" cy=".28" r=".2">
        <stop offset="0" stop-color="#d9402a" stop-opacity=".55"/>
        <stop offset="1" stop-color="#d9402a" stop-opacity="0"/>
      </radialGradient>
      <linearGradient id="titleShadeBack" x1="0" y1="0" x2="0" y2="1">
        <stop offset="0" stop-color="#000" stop-opacity="0"/>
        <stop offset="1" stop-color="#000" stop-opacity=".75"/>
      </linearGradient>
      <clipPath id="backPhotoClip"><polygon points="24,22 357,22 299,456 24,456"/></clipPath>
    </defs>
    <rect x="24" y="22" width="672" height="434" fill="var(--amber)"/>
    <g clip-path="url(#backPhotoClip)" role="img" aria-label="Photo of a boy in a white uniform, orange belt and red gloves in a kicking stance against a brick wall">
      <rect x="24" y="22" width="340" height="434" fill="url(#wallTone)"/>
      <rect x="24" y="22" width="340" height="434" fill="url(#fighterGlow)"/>
      <rect x="24" y="22" width="340" height="434" fill="url(#gloveTone)"/>
      <rect x="24" y="320" width="340" height="136" fill="url(#titleShadeBack)"/>
    </g>
    <polygon points="360,0 438,0 306,456 296,480" fill="var(--slate)"/>
    <rect x="604" y="54" width="66" height="66" fill="none" stroke="var(--ink)" stroke-width="1.6"/>
    <line x1="458" y1="256" x2="670" y2="256" stroke="var(--ink)" stroke-width="1.6"/>
    <line x1="394" y1="296" x2="670" y2="296" stroke="var(--ink)" stroke-width="1.6"/>
    <line x1="362" y1="336" x2="670" y2="336" stroke="var(--ink)" stroke-width="1.6"/>
  </svg>

  <div class="abs brand"><span class="brand-dot"></span>Kicks Dojo</div>
  <div class="abs photo-title">Children’s martial<br>art classes</div>
</section>

</body>
</html>
```